Nimbus Crest Plan- Brindlow Insurance providing specialist Cyber and Liability Insurance

for Managed Technology Service Providers and their customer, we will use a letterhead that white labels insurer documents, which can be used in our physical letters as well as to be used within Email signatures.

Target Market(s)

Managed Technology Services Providers

Industry/Entity Type

Cyber Insurance

Requirements
Must have
• website, email address, contact phone numbers

```html
<!DOCTYPE html>
<html lang="en">
<head>
<meta charset="utf-8">
<title>Nimbus Crest Plan — Letterhead</title>
<link href="https://fonts.googleapis.com/css2?family=Didact+Gothic&family=Mulish:wght@400;700;800&family=Open+Sans:wght@600&display=swap" rel="stylesheet">
<style>
  :root {
    --backdrop: #6b6b6b;
    --paper: #ffffff;
    --ink: #4a4a4a;
    --ink-soft: #6e6e6e;
    --brand-green: #4cba58;
    --sign-tone: #e9e9e9;
  }
  * { margin: 0; padding: 0; box-sizing: border-box; }
  html, body {
    width: 1024px; height: 1200px; overflow: hidden;
    background: var(--backdrop);
  }
  .letterhead {
    position: absolute; left: 109px; top: 30px;
    width: 806px; height: 1140px;
    background: var(--paper);
    color: var(--ink);
  }
  .brand-name {
    position: absolute; left: 32px; top: 60px;
    font-family: "Mulish", sans-serif; font-weight: 800;
    font-size: 24px; letter-spacing: 1px; color: var(--ink);
  }
  .brand-rule {
    position: absolute; left: 283px; right: 0; top: 81px;
    height: 1.5px; background: var(--brand-green);
  }
  .sender { position: absolute; left: 36px; top: 260px; font-family: "Mulish", sans-serif; }
  .sender-name { font-weight: 700; font-size: 26px; letter-spacing: .5px; margin-bottom: 10px; }
  .sender-line { font-size: 14.5px; line-height: 19px; margin-bottom: 7px; }
  .sender-address { font-size: 14.5px; line-height: 20px; }
  .letter-date {
    position: absolute; right: 38px; top: 368px;
    font-family: "Open Sans", sans-serif; font-weight: 600; font-size: 16.5px;
  }
  .letter-body {
    position: absolute; left: 32px; width: 736px;
    font-family: "Didact Gothic", sans-serif; font-size: 15.6px; line-height: 18.7px;
    letter-spacing: 0.35px;
    color: var(--ink-soft); text-align: justify;
    hyphens: auto; -webkit-hyphens: auto;
  }
  .body-one { top: 426px; }
  .body-two { top: 557px; }
  .body-three { top: 688px; }
  .signoff-title {
    position: absolute; left: 59px; top: 803px;
    font-family: "Didact Gothic", sans-serif; font-size: 21px; color: var(--ink);
  }
  .signature-area {
    position: absolute; left: 77px; top: 851px; width: 150px; height: 92px;
    background: var(--sign-tone); border-radius: 4px;
  }
  .contact-band {
    position: absolute; left: 0; right: 0; top: 1056px; height: 36px;
    background: var(--brand-green); color: var(--paper);
    display: flex; align-items: center; justify-content: center; gap: 10px;
    font-family: "Didact Gothic", sans-serif; font-size: 15.5px;
  }
  .contact-item { display: flex; align-items: center; gap: 4px; }
  .contact-item svg { width: 14px; height: 14px; }
</style>
</head>
<body>
<main class="letterhead">
  <div class="brand-name">Nimbus Crest Plan</div>
  <div class="brand-rule"></div>

  <section class="sender">
    <h1 class="sender-name">MARA ELLISON</h1>
    <p class="sender-line">0145-672-318</p>
    <p class="sender-line">info@nimbuscrestplan.com</p>
    <p class="sender-address">4870 Harlow Ridge Rd. Suite<br>210 Fenwick, OR 0000</p>
  </section>
  <p class="letter-date">12 December, 2023</p>

  <p class="letter-body body-one" lang="la">Lorem ipsum dolor sit amet, consectetuer adipiscing elit, sed diam nonummy nibh euismod tincidunt ut laoreet dolore magna aliquam erat volutpat. Ut wisi enim ad minim veniam, quis nostrud exerci tation ullamcorper suscipit lobortis nisl ut aliquip ex ea commodo consequat. Duis autem vel eum iriure dolor in hendrerit in vulputate velit esse molestie consequat, vel illum dolore eu feugiat nulla facilisis at vero eros et accumsan et iusto odio dignissim qui blandit praesent luptatum zzril delenit augue duis dolore te feugait nulla facilisi.</p>
  <p class="letter-body body-two" lang="la">Lorem ipsum dolor sit amet, cons ectetuer adipiscing elit, sed diam nonummy nibh euismod tincidunt ut laoreet dolore magna aliquam erat volutpat. Ut wisi enim ad minim veniam, quis nostrud exerci tation ullamcorper suscipit lobortis nisl ut aliquip ex ea commodo consequat.<br>Lorem ipsum dolor sit amet, consectetuer adipiscing elit, sed diam nonummy nibh euismod tincidunt ut laoreet dolore magna aliquam erat</p>
  <p class="letter-body body-three" lang="la">Lorem ipsum dolor sit amet, cons ectetuer adipiscing elit, sed diam nonummy nibh euismod tincidunt ut laoreet dolore magna aliquam erat volutpat. Ut wisi enim ad minim veniam, quis nostrud exerci tation ullamcorper suscipit lobortis nisl ut aliquip ex ea commodo consequat. Lorem ipsum dolor sit zamet, consectetuer adipiscing elit, sed diam nonummy nibh euismod tincidunt.</p>

  <p class="signoff-title">Managing Director</p>
  <div class="signature-area" role="img" aria-label="Handwritten signature of the managing director"></div>

  <footer class="contact-band">
    <span class="contact-item">
      <svg viewBox="0 0 16 16"><circle cx="8" cy="8" r="8" fill="#fff"/><path d="M5.5 4.5l1.3 0 .7 1.8-.9.7c.5 1 1.3 1.8 2.3 2.3l.7-.9 1.8.7v1.3c0 .5-.5.9-1 .8C7.5 11.6 4.4 8.5 4.1 5.5c0-.5.4-1 .9-1z" fill="#4cba58"/></svg>
      0145-672-318
    </span>
    <span class="contact-item">
      <svg viewBox="0 0 16 16"><circle cx="8" cy="8" r="8" fill="#fff"/><rect x="4" y="5" width="8" height="6" rx="1" fill="#4cba58"/><path d="M4.3 5.5L8 8.3l3.7-2.8" stroke="#fff" stroke-width="1" fill="none"/></svg>
      info@nimbuscrestplan.com
    </span>
    <span class="contact-item">
      <svg viewBox="0 0 16 16"><circle cx="8" cy="8" r="7" fill="none" stroke="#fff" stroke-width="1.4"/><ellipse cx="8" cy="8" rx="3" ry="7" fill="none" stroke="#fff" stroke-width="1"/><path d="M1 8h14M2.5 4.5h11M2.5 11.5h11" stroke="#fff" stroke-width="1"/></svg>
      www.nimbuscrestplan.com
    </span>
  </footer>
</main>
</body>
</html>
```